Gourmet butcher shop needs a business card design

We need a business card design for an upmarket butcher shop in Brisbane, Queensland Australia. We would prefer the card to be printed on a brown craft paper business card and would consider the use of raised print on the card. The card needs to make space for the usual information: ABN, address, telephone, facebook page. I stress it is a gourmet shop in a wealthy suburb. Thanks

Industry/Entity Type

Business

Contact Information for Business Card

Address Shop 2, Wendmoor Arcade, 417 Purlow Street, Wendmoor
Telephone 07 5914 3027
A.B.N. 73 508 914 226
Facebook www.fakebooksite.example/wendmoorarcadecuts

Requirements
Should not have
• No need for a person's name or title

```html
<!DOCTYPE html>
<html lang="en">
<head>
<meta charset="utf-8">
<title>Wendmoor Arcade Cuts – Business Card</title>
<link rel="stylesheet" href="https://fonts.googleapis.com/css2?family=Arimo:wght@400;700&display=swap">
<style>
  :root {
    --bg: #e9e6e1;
    --brand-red: #c8202f;
    --card-white: #ffffff;
    --ink-dark: #2b2b2b;
    --ink-grey: #6f6f6f;
    --rule-grey: #d3d3d3;
  }
  * { box-sizing: border-box; margin: 0; padding: 0; }
  html, body {
    width: 1200px; height: 950px; overflow: hidden;
    background: var(--bg);
    font-family: "Arimo", Arial, sans-serif;
  }
  .canvas { position: relative; width: 1200px; height: 950px; }
  .card {
    position: absolute; left: 250px; width: 700px; height: 400px;
    box-shadow: 0 10px 24px rgba(0,0,0,0.18);
    overflow: hidden;
  }
  /* Front */
  .card-front { top: 50px; background: var(--brand-red); color: var(--card-white); }
  .front-brand {
    position: absolute; left: 0; right: 0; top: 112px;
    text-align: center; font-weight: 700; color: var(--card-white); line-height: 1;
  }
  .front-brand .brand-line-1 { font-size: 30px; letter-spacing: 3px; }
  .front-brand .brand-line-2 { font-size: 84px; letter-spacing: 6px; margin-top: 8px; }
  .front-web {
    position: absolute; left: 0; right: 0; top: 290px;
    text-align: center; font-size: 18px; letter-spacing: 4px;
  }
  /* Back */
  .card-back { top: 500px; background: var(--card-white); }
  .back-brand {
    position: absolute; left: 40px; width: 340px; top: 62px;
    text-align: center; font-weight: 700; color: var(--brand-red); line-height: 1;
  }
  .back-brand .brand-line-1 { font-size: 20px; letter-spacing: 2px; }
  .back-brand .brand-line-2 { font-size: 62px; letter-spacing: 5px; margin-top: 6px; }
  .shop-address {
    position: absolute; right: 330px; top: 200px; text-align: right;
    font-size: 17px; color: var(--ink-grey); line-height: 1.45;
  }
  .divider {
    position: absolute; left: 395px; top: 70px; width: 1px; height: 225px;
    background: var(--rule-grey);
  }
  .contact-list {
    position: absolute; left: 418px; top: 82px; list-style: none;
    font-size: 16px; color: var(--ink-grey);
  }
  .contact-list li { display: flex; align-items: center; height: 31px; white-space: nowrap; }
  .contact-list svg { width: 16px; height: 16px; margin-right: 8px; flex: none; }
  .band-line {
    position: absolute; left: 0; right: 0; bottom: 48px; height: 3px; background: var(--ink-dark);
  }
  .band {
    position: absolute; left: 0; right: 0; bottom: 0; height: 44px; background: var(--brand-red);
  }
</style>
</head>
<body>
<main class="canvas">
  <section class="card card-front">
    <div class="front-brand">
      <div class="brand-line-1">WENDMOOR ARCADE</div>
      <div class="brand-line-2">CUTS</div>
    </div>
    <div class="front-web">www.example.com</div>
  </section>

  <section class="card card-back">
    <div class="back-brand">
      <div class="brand-line-1">WENDMOOR ARCADE</div>
      <div class="brand-line-2">CUTS</div>
    </div>

    <div class="shop-address">
      Shop 2, Wendmoor Arcade<br>
      417 Purlow Street<br>
      Wendmoor
    </div>

    <div class="divider"></div>

    <ul class="contact-list">
      <li>ABN 73 508 914 226</li>
      <li>
        <svg viewBox="0 0 16 16" aria-hidden="true"><path fill="var(--brand-red)" d="M4 1.5l2.2 3-1.3 1.6a9 9 0 0 0 5 5l1.6-1.3 3 2.2-1.4 2.4C8 14.6 1.4 8 1.6 2.9z"/></svg>
        07 5914 3027
      </li>
      <li>
        <svg viewBox="0 0 16 16" aria-hidden="true"><rect x="1" y="3.5" width="14" height="9" rx="1" fill="var(--brand-red)"/><path d="M1.5 4l6.5 5 6.5-5" stroke="#fff" stroke-width="1.2" fill="none"/></svg>
        hello@example.com
      </li>
      <li>
        <svg viewBox="0 0 16 16" aria-hidden="true"><circle cx="8" cy="8" r="7" fill="var(--brand-red)"/><path d="M1 8h14M8 1c-3 3.5-3 10.5 0 14M8 1c3 3.5 3 10.5 0 14" stroke="#fff" stroke-width="1" fill="none"/></svg>
        www.example.com
      </li>
      <li>
        <svg viewBox="0 0 16 16" aria-hidden="true"><rect x="1.5" y="1.5" width="13" height="13" rx="2" fill="var(--brand-red)"/></svg>
        wendmoorarcadecuts
      </li>
    </ul>

    <div class="band-line"></div>
    <div class="band"></div>
  </section>
</main>
</body>
</html>
```